I am a company selling interior designing materials

HI, I am selling interior design materials and require a namecard which is more outstanding while following a certain details placement as attached.

My clients are mainly interior designers so it has to attract their attention rather than feeling that its "just another namecard". I am selling wallcoverings, fabrics, acoustics and carpets.

Target Market(s)

interior designers designing hotels, commerical offices.

Contact Information for Business Card

As per attached.
Please change address to 47 Jalan 16 Tampines #05-02 Velmora Building Singapore 527314

Font styles to use
Other font styles liked:
• calibri

Requirements
Must have
• (1) company logo on top in the middle. Placement of contac details to be the same
• (2) company color is blue/green cymk 75/8/42/0
• (3) "KTV" logo to be prominent
• (4) You may change the logo but there should be a "swirl" surrounding the word KTV like current logo. The swirl pattern does not need to follow current logo and you may propose.
Should not have
• (1) there should not be any designs above "KTV" logo
• (2) no sharp triangles or angles

```html
<!DOCTYPE html>
<html lang="en">
<head>
<meta charset="utf-8">
<title>KTV Furnishings – Business Card</title>
<link href="https://fonts.googleapis.com/css2?family=Montserrat:wght@400;500;600;800&display=swap" rel="stylesheet">
<style>
  :root{
    --teal:#2fb0a3;
    --teal-deep:#23998e;
    --teal-light:#45c2b5;
    --ink:#3d3f42;
    --logo-grey:#6b6d70;
    --logo-light:#eef2f1;
    --paper:#ffffff;
    --stage:#e9ecec;
  }
  *{box-sizing:border-box;margin:0;padding:0}
  html,body{width:1200px;height:900px;overflow:hidden;background:var(--stage);font-family:"Montserrat",sans-serif}
  .stage{position:relative;width:1200px;height:900px}
  .card{position:absolute;left:280px;width:640px;height:366px;border-radius:22px;overflow:hidden;box-shadow:0 10px 30px rgba(0,0,0,.15)}
  .card--back{top:48px;background:linear-gradient(160deg,var(--teal-light),var(--teal-deep))}
  .card--front{top:486px;background:var(--paper)}

  /* back */
  .back-logo{position:absolute;left:0;right:0;top:92px;text-align:center;font-weight:800;font-size:110px;letter-spacing:4px;color:var(--logo-light);line-height:1}
  .services{position:absolute;left:0;right:0;bottom:72px;display:flex;justify-content:center;gap:30px;color:#fff;font-size:17px;font-weight:400;letter-spacing:.5px}
  .service{display:flex;align-items:center;gap:8px}
  .service svg{width:16px;height:16px}

  /* front */
  .front-logo{position:absolute;right:58px;top:96px;font-weight:800;font-size:68px;letter-spacing:2px;color:var(--logo-grey);line-height:1}
  .person{position:absolute;left:40px;top:150px}
  .person__name{font-size:24px;font-weight:600;color:var(--teal)}
  .person__role{font-size:14px;font-weight:500;color:var(--ink);letter-spacing:2px;margin-top:2px}
  .rule{position:absolute;left:232px;right:40px;top:192px;height:2px;background:var(--teal)}
  .contacts{position:absolute;left:40px;top:222px;display:grid;grid-template-columns:250px 1fr;row-gap:14px;font-size:14px;color:var(--ink)}
  .contact{display:flex;align-items:center;gap:9px}
  .contact svg{width:20px;height:20px;flex:none}
  .address{position:absolute;left:40px;top:300px;font-size:15px;font-weight:600;color:var(--teal)}
  .band{position:absolute;left:0;right:0;bottom:0;height:14px;background:var(--teal)}
</style>
</head>
<body>
<main class="stage">

  <section class="card card--back" aria-label="Business card back">
    <div class="back-logo">KTV</div>
    <ul class="services" style="list-style:none">
      <li class="service"><svg viewBox="0 0 16 16"><circle cx="8" cy="8" r="7" fill="none" stroke="#fff" stroke-width="1.2"/><path d="M4.8 8.2l2.2 2.2 4.2-4.4" fill="none" stroke="#fff" stroke-width="1.4" stroke-linecap="round" stroke-linejoin="round"/></svg>Wallcoverings</li>
      <li class="service"><svg viewBox="0 0 16 16"><circle cx="8" cy="8" r="7" fill="none" stroke="#fff" stroke-width="1.2"/><path d="M4.8 8.2l2.2 2.2 4.2-4.4" fill="none" stroke="#fff" stroke-width="1.4" stroke-linecap="round" stroke-linejoin="round"/></svg>Acoustic</li>
      <li class="service"><svg viewBox="0 0 16 16"><circle cx="8" cy="8" r="7" fill="none" stroke="#fff" stroke-width="1.2"/><path d="M4.8 8.2l2.2 2.2 4.2-4.4" fill="none" stroke="#fff" stroke-width="1.4" stroke-linecap="round" stroke-linejoin="round"/></svg>Fabrics</li>
      <li class="service"><svg viewBox="0 0 16 16"><circle cx="8" cy="8" r="7" fill="none" stroke="#fff" stroke-width="1.2"/><path d="M4.8 8.2l2.2 2.2 4.2-4.4" fill="none" stroke="#fff" stroke-width="1.4" stroke-linecap="round" stroke-linejoin="round"/></svg>Carpet</li>
    </ul>
  </section>

  <section class="card card--front" aria-label="Business card front">
    <div class="front-logo">KTV</div>
    <div class="person">
      <h1 class="person__name">Sharon Lim</h1>
      <p class="person__role">Interior Designer</p>
    </div>
    <div class="rule"></div>
    <div class="contacts">
      <div class="contact">
        <svg viewBox="0 0 20 20"><circle cx="10" cy="10" r="10" fill="var(--teal)"/><rect x="7" y="4.5" width="6" height="11" rx="1.2" fill="none" stroke="#fff" stroke-width="1.3"/><circle cx="10" cy="13.3" r=".8" fill="#fff"/></svg>
        (65) 9172 4035
      </div>
      <div class="contact">
        <svg viewBox="0 0 20 20"><circle cx="10" cy="10" r="10" fill="var(--teal)"/><path d="M5 8.5c0-2 2.2-3 5-3s5 1 5 3l-1.8.6-.7-1.6h-5l-.7 1.6z" fill="#fff"/><rect x="6" y="10" width="8" height="4.5" rx="1" fill="#fff"/></svg>
        (65) 6283 1947
      </div>
      <div class="contact">
        <svg viewBox="0 0 20 20"><circle cx="10" cy="10" r="10" fill="var(--teal)"/><rect x="5" y="6.5" width="10" height="7" rx="1" fill="none" stroke="#fff" stroke-width="1.2"/><path d="M5.3 7l4.7 3.6L14.7 7" fill="none" stroke="#fff" stroke-width="1.2"/></svg>
        sharon@ktvfurnishings.com
      </div>
      <div class="contact">
        <svg viewBox="0 0 20 20"><circle cx="10" cy="10" r="10" fill="var(--teal)"/><rect x="4.5" y="8" width="6" height="4" rx="2" fill="none" stroke="#fff" stroke-width="1.3" transform="rotate(-40 7.5 10)"/><rect x="9.5" y="8" width="6" height="4" rx="2" fill="none" stroke="#fff" stroke-width="1.3" transform="rotate(-40 12.5 10)"/></svg>
        www.ktvfurnishings.com
      </div>
    </div>
    <p class="address">47 Jalan 16 Tampines #05-02 Velmora Building Singapore 527314</p>
    <div class="band"></div>
  </section>

</main>
</body>
</html>
```